We have a new logo so we need to change our business card

We're super Happy with our current cards but I think with a new logo should come a new design. I wouldn't mind seeing the icons that we used on the back last time reused on this card. Please feel free to visit our website to get a sense for our brand www.brindlewick.ca

I need the final final to have contact info for:

Gordon Hasley
Co-Owner
info@brindlewick.ca
778-315-6207

and

Marjorie Hasley
Co-Owner
info@brindlewick.ca
778-342-5810

Target Market(s)

Female dog owners, 21 to 70

Industry/Entity Type

pet industry

Contact Information for Business Card

included in brief

Requirements
Should not have
• We do not want it to look cartonish

```html
<!DOCTYPE html>
<html lang="en">
<head>
<meta charset="utf-8">
<title>Brindlewick Business Card</title>
<link rel="stylesheet" href="https://fonts.googleapis.com/css2?family=Arimo:wght@400;700&display=swap">
<style>
  :root {
    --backdrop: #262626;
    --card: #151515;
    --green: #7dc855;
    --white: #ffffff;
    --text: #f2f2f2;
  }
  * { margin: 0; padding: 0; box-sizing: border-box; }
  html, body {
    width: 1200px; height: 1059px; overflow: hidden;
    background: var(--backdrop);
    font-family: "Arimo", Arial, sans-serif;
  }
  .canvas { position: relative; width: 1200px; height: 1059px; }
  .card {
    position: absolute; left: 255px; width: 690px; height: 392px;
    background: var(--card);
    box-shadow: 0 10px 24px rgba(0,0,0,0.55);
  }
  .card-front { top: 90px; }
  .card-back { top: 547px; }

  .brand { position: absolute; display: flex; align-items: center; }
  .brand-mark { border-radius: 50%; background: var(--green); flex: none; }
  .brand-name { color: var(--white); font-weight: 700; line-height: 1; letter-spacing: -0.5px; }

  .card-front .brand { left: 45px; top: 162px; }
  .card-front .brand-mark { width: 70px; height: 70px; margin-right: 10px; }
  .card-front .brand-name { font-size: 34px; }

  .divider { position: absolute; left: 343px; top: 118px; width: 1.5px; height: 155px; background: var(--green); }

  .contact-block { position: absolute; left: 372px; top: 116px; }
  .person-name { color: var(--green); font-weight: 700; font-size: 23px; letter-spacing: 0.3px; text-transform: uppercase; }
  .person-role { color: var(--text); font-size: 19px; margin-top: 3px; }
  .contact-list { list-style: none; margin-top: 16px; }
  .contact-item { display: flex; align-items: center; color: var(--text); font-size: 19px; height: 31.5px; }
  .contact-icon { width: 20px; height: 20px; margin-right: 7px; flex: none; }

  .card-back .brand { left: 284px; top: 31px; }
  .card-back .brand-mark { width: 98px; height: 98px; margin-right: 10px; }
  .card-back .brand-name { font-size: 47px; }

  .benefits { position: absolute; left: 29px; top: 141px; }
  .benefits-title { color: var(--green); font-weight: 700; font-size: 30px; letter-spacing: 0.3px; }
  .benefit-list { list-style: none; margin-top: 12px; }
  .benefit-item { color: var(--text); font-size: 17.5px; height: 25.6px; display: flex; align-items: center; }
  .benefit-item::before {
    content: ""; width: 6px; height: 6px; border-radius: 50%;
    background: var(--green); margin-right: 6px; flex: none;
  }

  .badge {
    position: absolute; width: 62px; height: 62px; border-radius: 50%;
    border: 3px solid var(--white); background: var(--card);
  }
  .badge::after {
    content: ""; position: absolute; inset: 5px; border-radius: 50%;
    border: 1.5px solid var(--white);
  }
  .badge-1 { left: 440px; top: 220px; }
  .badge-2 { left: 513px; top: 220px; }
  .badge-3 { left: 591px; top: 220px; }
  .badge-4 { left: 474px; top: 295px; }
  .badge-5 { left: 561px; top: 295px; }
</style>
</head>
<body>
<main class="canvas">

  <section class="card card-front">
    <div class="brand">
      <div class="brand-mark"></div>
      <span class="brand-name">Brindlewick</span>
    </div>

    <div class="divider"></div>

    <div class="contact-block">
      <h1 class="person-name">Gordon Hasley</h1>
      <p class="person-role">Co-Owner</p>
      <ul class="contact-list">
        <li class="contact-item">
          <svg class="contact-icon" viewBox="0 0 20 20" aria-hidden="true">
            <circle cx="10" cy="10" r="10" fill="#7dc855"/>
            <path d="M6.2 5.2l2 -.3 1 2.4-1.2 1c.6 1.3 1.6 2.3 2.9 2.9l1-1.2 2.4 1-.3 2c-4.4.3-8.1-3.4-7.8-7.8z" fill="#151515"/>
          </svg>
          778-315-6207
        </li>
        <li class="contact-item">
          <svg class="contact-icon" viewBox="0 0 20 20" aria-hidden="true">
            <circle cx="10" cy="10" r="10" fill="#7dc855"/>
            <rect x="5" y="6.5" width="10" height="7" fill="none" stroke="#151515" stroke-width="1.4"/>
            <path d="M5 6.5l5 4 5-4M5 13.5l3.5-3.5M15 13.5l-3.5-3.5" fill="none" stroke="#151515" stroke-width="1.2"/>
          </svg>
          info@brindlewick.ca
        </li>
        <li class="contact-item">
          <svg class="contact-icon" viewBox="0 0 20 20" aria-hidden="true">
            <circle cx="10" cy="10" r="10" fill="#7dc855"/>
            <circle cx="10" cy="10" r="5.5" fill="none" stroke="#151515" stroke-width="1.3"/>
            <path d="M4.5 10h11M10 4.5c-2.5 3-2.5 8 0 11M10 4.5c2.5 3 2.5 8 0 11" fill="none" stroke="#151515" stroke-width="1.1"/>
          </svg>
          www.brindlewick.ca
        </li>
      </ul>
    </div>
  </section>

  <section class="card card-back">
    <div class="brand">
      <div class="brand-mark"></div>
      <span class="brand-name">Brindlewick</span>
    </div>

    <div class="benefits">
      <h2 class="benefits-title">BENEFITS</h2>
      <ul class="benefit-list">
        <li class="benefit-item">Improves condition of the skin and fur</li>
        <li class="benefit-item">Reduces shedding and dandruff</li>
        <li class="benefit-item">Strengthens the immune system</li>
        <li class="benefit-item">Helps eliminate unwanted odours</li>
        <li class="benefit-item">Adds a scented benefit</li>
        <li class="benefit-item">Helps with; anxiety, arthritis, insomnia</li>
        <li class="benefit-item">drowsiness, skin rritation &amp; depression</li>
      </ul>
    </div>

    <div class="badge badge-1"></div>
    <div class="badge badge-2"></div>
    <div class="badge badge-3"></div>
    <div class="badge badge-4"></div>
    <div class="badge badge-5"></div>
  </section>

</main>
</body>
</html>
```